2 Wine Label Designs

Vintner Bloom has been helping people give customized wine gifts since 1999. From large scale corporate clients, to 1 bottle personalized gifts, we offer a wide range of wines and templates for any occasion. Recently we’ve started to shift our focus to a younger demographic (21 to 35 year old women) and are in the process of updating our website and branding.

One big area we’re working to improve is the customizable wine label/engraving templates we offer on the site (to see our current template library go to www.vintnerbloom-demo.com/shop/wine, select a wine, choose “label” or “engraving” from the dropdown, and click “customize”). You’ll find that a lot of our current templates are outdated or aimed at an older demographic. Over the next few months we want to swap out most of these old templates with fun fresh designs.

We're asking designers to submit 2 customizable wine label templates for this project. One should be wedding themed and the other "Thank You" themed. Please see the attached PDF for more guidelines and creative direction.

Keep in mind, even if you aren't selected as the winner of this project we are going to go through and offer $50 for any label template submitted that we like ($100 if we want both). So there is a good chance you'll be getting some money for your work!

Please read though the attached guidelines PDF carefully (especially the "Must be Customizable" section).

Target Market(s)

21 to 35 year old women

Colors

Designer to choose colors to be used in the design.

Requirements
Must have
• See attached PDF
Nice to have
• See attached PDF
Should not have
• See attached PDF

```html
<!DOCTYPE html>
<html lang="en">
<head>
<meta charset="utf-8">
<title>Wedding Wine Label Templates</title>
<link rel="stylesheet" href="https://fonts.googleapis.com/css2?family=Nunito:wght@500&family=Pinyon+Script&family=Great+Vibes&family=Libre+Baskerville&display=swap">
<style>
  :root{
    --page:#ffffff;
    --ink:#1d1d1d;
    --pink-edge:#ebb4c5;
    --cream:#f7ebdc;
    --cream-mid:#f1d9cb;
    --lace:#d9808f;
    --band:#e4d3bb;
    --brown:#4f3c37;
    --brown-soft:#8a716a;
    --sign-fill:#f9dcd6;
    --sign-ink:#c9717c;
    --doily:#f2b8bd;
    --photo:#f8d4cd;
    --photo-ring:#c9717c;
    --rope:#8b8069;
    --tassel:#a59480;
  }
  *{margin:0;padding:0;box-sizing:border-box}
  html,body{width:1200px;height:1200px;overflow:hidden;background:var(--page)}
  .sheet{position:relative;width:1200px;height:1200px}
  .sheet-title{position:absolute;font-family:"Nunito",sans-serif;font-weight:500;font-size:42px;letter-spacing:.14em;color:var(--ink);transform:translateX(-50%);white-space:nowrap;line-height:1}
  .title-wide{left:862px;top:68px}
  .title-tall{left:274px;top:264px}
  .title-square{left:302px;top:1090px}
  .template{position:absolute;display:block}
  .template-wide{left:547px;top:118px}
  .template-tall{left:27px;top:320px}
  .template-square{left:547px;top:643px}
  .lace{fill:var(--lace)}
  .band{fill:var(--band)}
  .rope{fill:none;stroke:var(--rope);stroke-width:1.6}
  .chain{stroke:var(--brown-soft);stroke-width:2;stroke-dasharray:4 2}
  .tassel{fill:var(--tassel)}
  .scroll{fill:none;stroke:var(--brown);stroke-width:2}
  .sign{fill:var(--sign-fill);stroke:var(--brown);stroke-width:1.4}
  .sign-inner{fill:none;stroke:var(--brown);stroke-width:.8;stroke-dasharray:3 2}
  .doily{fill:var(--doily)}
  .photo{fill:var(--photo);stroke:var(--photo-ring);stroke-width:3}
  .carriage{fill:var(--brown);opacity:.85}
  .rule{stroke:var(--brown);stroke-width:1.2}
  .couple-name,.photo-label{font-family:"Pinyon Script",cursive;fill:var(--sign-ink)}
  .lived{font-family:"Libre Baskerville",serif;fill:var(--brown);letter-spacing:.02em}
  .happily{font-family:"Great Vibes",cursive;fill:var(--brown);font-weight:700;stroke:var(--brown);stroke-width:.6}
  .detail{font-family:"Libre Baskerville",serif;fill:var(--brown)}
</style>
</head>
<body>
<main class="sheet">

  <h2 class="sheet-title title-wide">WIDE TEMPLATE</h2>
  <svg class="template template-wide" width="626" height="486" viewBox="0 0 626 486">
    <defs>
      <linearGradient id="bg-wide" x1="0" x2="1" y1="0" y2="0">
        <stop offset="0" stop-color="var(--pink-edge)"/>
        <stop offset=".12" stop-color="var(--cream-mid)"/>
        <stop offset=".5" stop-color="var(--cream)"/>
        <stop offset=".88" stop-color="var(--cream-mid)"/>
        <stop offset="1" stop-color="var(--pink-edge)"/>
      </linearGradient>
    </defs>
    <rect width="626" height="486" fill="url(#bg-wide)"/>
    <rect class="lace" x="0" y="0" width="626" height="38" role="img" aria-label="Pink lace border pattern"/>
    <path class="rope" d="M0 14 Q300 90 626 30"/>
    <path class="rope" d="M60 6 Q330 70 600 10"/>
    <line class="chain" x1="69" y1="2" x2="69" y2="122"/>
    <line class="chain" x1="297" y1="2" x2="297" y2="122"/>
    <rect class="tassel" x="553" y="0" width="8" height="202" role="img" aria-label="Hanging tassel"/>
    <rect class="tassel" x="585" y="0" width="8" height="154" role="img" aria-label="Hanging tassel"/>
    <rect class="scroll" x="60" y="98" width="246" height="20" rx="10" role="img" aria-label="Scrollwork ornament"/>
    <rect class="sign" x="37" y="131" width="292" height="59" rx="8"/>
    <rect class="sign-inner" x="43" y="137" width="280" height="47" rx="6"/>
    <text class="couple-name" x="182" y="169" font-size="29" text-anchor="middle">“Couple Name Here”</text>
    <rect class="scroll" x="60" y="196" width="246" height="20" rx="10" role="img" aria-label="Scrollwork ornament"/>
    <line class="rule" x1="49" y1="242" x2="317" y2="242"/>
    <text class="lived" x="182" y="262" font-size="15" text-anchor="middle">AND THEY LIVED</text>
    <text class="happily" x="182" y="303" font-size="42" text-anchor="middle">Happily Ever After</text>
    <line class="rule" x1="49" y1="315" x2="317" y2="315"/>
    <circle class="doily" cx="470" cy="200" r="124" role="img" aria-label="Lace doily photo frame"/>
    <circle class="photo" cx="470" cy="200" r="88"/>
    <text class="photo-label" x="470" y="207" font-size="22" text-anchor="middle">“Photo Here”</text>
    <rect class="lace" x="0" y="358" width="626" height="29" role="img" aria-label="Pink lace border pattern"/>
    <rect class="band" x="0" y="387" width="626" height="48"/>
    <rect class="lace" x="0" y="435" width="626" height="31" role="img" aria-label="Pink lace border pattern"/>
    <rect class="carriage" x="32" y="326" width="245" height="108" rx="10" role="img" aria-label="Silhouette of a royal carriage drawn by a horse"/>
    <text class="detail" x="359" y="414" font-size="11" text-anchor="middle">“Date Text Here”</text>
    <text class="detail" x="534" y="414" font-size="11" text-anchor="middle">“Reception Text Here”</text>
  </svg>

  <h2 class="sheet-title title-tall">TALL TEMPLATE</h2>
  <svg class="template template-tall" width="490" height="629" viewBox="0 0 490 629">
    <defs>
      <linearGradient id="bg-tall" x1="0" x2="1" y1="0" y2="0">
        <stop offset="0" stop-color="var(--pink-edge)"/>
        <stop offset=".14" stop-color="var(--cream-mid)"/>
        <stop offset=".5" stop-color="var(--cream)"/>
        <stop offset=".86" stop-color="var(--cream-mid)"/>
        <stop offset="1" stop-color="var(--pink-edge)"/>
      </linearGradient>
    </defs>
    <rect width="490" height="629" fill="url(#bg-tall)"/>
    <rect class="lace" x="0" y="0" width="490" height="36" role="img" aria-label="Pink lace border pattern"/>
    <path class="rope" d="M0 14 Q240 80 490 24"/>
    <path class="rope" d="M40 6 Q260 62 470 8"/>
    <line class="chain" x1="77" y1="4" x2="77" y2="116"/>
    <line class="chain" x1="305" y1="4" x2="305" y2="116"/>
    <rect class="tassel" x="398" y="0" width="8" height="184" role="img" aria-label="Hanging tassel"/>
    <rect class="tassel" x="430" y="0" width="8" height="140" role="img" aria-label="Hanging tassel"/>
    <rect class="scroll" x="68" y="92" width="246" height="20" rx="10" role="img" aria-label="Scrollwork ornament"/>
    <rect class="sign" x="45" y="118" width="292" height="68" rx="8"/>
    <rect class="sign-inner" x="51" y="124" width="280" height="56" rx="6"/>
    <text class="couple-name" x="190" y="162" font-size="29" text-anchor="middle">“Couple Name Here”</text>
    <rect class="scroll" x="68" y="191" width="246" height="20" rx="10" role="img" aria-label="Scrollwork ornament"/>
    <circle class="doily" cx="337" cy="332" r="124" role="img" aria-label="Lace doily photo frame"/>
    <circle class="photo" cx="337" cy="332" r="86"/>
    <text class="photo-label" x="337" y="339" font-size="22" text-anchor="middle">“Photo Here”</text>
    <line class="rule" x1="25" y1="266" x2="205" y2="266"/>
    <text class="lived" x="115" y="297" font-size="14" text-anchor="middle">AND THEY LIVED</text>
    <text class="happily" x="115" y="340" font-size="44" text-anchor="middle">Happily</text>
    <text class="happily" x="115" y="384" font-size="44" text-anchor="middle">Ever After</text>
    <line class="rule" x1="25" y1="410" x2="205" y2="410"/>
    <text class="detail" x="115" y="434" font-size="12" text-anchor="middle">“Date Text Here”</text>
    <rect class="lace" x="0" y="488" width="490" height="28" role="img" aria-label="Pink lace border pattern"/>
    <rect class="band" x="0" y="516" width="490" height="62"/>
    <rect class="lace" x="0" y="578" width="490" height="30" role="img" aria-label="Pink lace border pattern"/>
    <rect class="carriage" x="22" y="468" width="255" height="108" rx="10" role="img" aria-label="Silhouette of a royal carriage drawn by a horse"/>
    <text class="detail" x="380" y="550" font-size="11" text-anchor="middle">“Reception Text Here”</text>
  </svg>

  <h2 class="sheet-title title-square">SQUARE TEMPLATE</h2>
  <svg class="template template-square" width="487" height="487" viewBox="0 0 487 487">
    <defs>
      <linearGradient id="bg-square" x1="0" x2="1" y1="0" y2="0">
        <stop offset="0" stop-color="var(--pink-edge)"/>
        <stop offset=".14" stop-color="var(--cream-mid)"/>
        <stop offset=".5" stop-color="var(--cream)"/>
        <stop offset=".86" stop-color="var(--cream-mid)"/>
        <stop offset="1" stop-color="var(--pink-edge)"/>
      </linearGradient>
    </defs>
    <rect width="487" height="487" fill="url(#bg-square)"/>
    <rect class="lace" x="0" y="0" width="487" height="33" role="img" aria-label="Pink lace border pattern"/>
    <path class="rope" d="M0 12 Q240 76 487 22"/>
    <path class="rope" d="M40 5 Q260 56 470 8"/>
    <line class="chain" x1="58" y1="1" x2="58" y2="109"/>
    <line class="chain" x1="241" y1="1" x2="241" y2="109"/>
    <rect class="tassel" x="402" y="0" width="8" height="173" role="img" aria-label="Hanging tassel"/>
    <rect class="tassel" x="431" y="0" width="8" height="133" role="img" aria-label="Hanging tassel"/>
    <rect class="scroll" x="52" y="94" width="196" height="17" rx="8" role="img" aria-label="Scrollwork ornament"/>
    <rect class="sign" x="33" y="121" width="232" height="40" rx="7"/>
    <rect class="sign-inner" x="38" y="126" width="222" height="30" rx="5"/>
    <text class="couple-name" x="149" y="149" font-size="23" text-anchor="middle">“Couple Name Here”</text>
    <rect class="scroll" x="52" y="166" width="196" height="17" rx="8" role="img" aria-label="Scrollwork ornament"/>
    <circle class="doily" cx="363" cy="245" r="100" role="img" aria-label="Lace doily photo frame"/>
    <circle class="photo" cx="363" cy="245" r="70"/>
    <text class="photo-label" x="363" y="251" font-size="18" text-anchor="middle">“Photo Here”</text>
    <line class="rule" x1="45" y1="229" x2="253" y2="229"/>
    <text class="lived" x="149" y="251" font-size="12" text-anchor="middle">AND THEY LIVED</text>
    <text class="happily" x="149" y="284" font-size="32" text-anchor="middle">Happily Ever After</text>
    <line class="rule" x1="45" y1="298" x2="253" y2="298"/>
    <text class="detail" x="149" y="318" font-size="10" text-anchor="middle">“Date Text Here”</text>
    <rect class="lace" x="0" y="377" width="487" height="24" role="img" aria-label="Pink lace border pattern"/>
    <rect class="band" x="0" y="401" width="487" height="44"/>
    <rect class="lace" x="0" y="445" width="487" height="28" role="img" aria-label="Pink lace border pattern"/>
    <rect class="carriage" x="27" y="349" width="218" height="96" rx="9" role="img" aria-label="Silhouette of a royal carriage drawn by a horse"/>
    <text class="detail" x="350" y="426" font-size="8" text-anchor="middle">“Reception Text Here”</text>
  </svg>

</main>
</body>
</html>
```